Web Design Project

I need designs (PSD only - no programming) for several pages of a new website helping train operators to manage key information about their traindrivers.
The main feature of this website is the management of personnel records (create, edit, search, delete). Another key aspect is the management of user privileges. Since this is a new website we also need a user friendly frontpage, pricing information and how it works sections.
This can be broken down into 9 pages for which we need designs (PSDs).
1. Home
2. Driver record
3. How it works
4. Pricing
5. User administration
6. Help
7. Record list view
8. Login
9. Registration
Navigation (not logged in) are: Home | How it works | Pricing | Customers | About us | Contact
Navigation (logged in) are: Overview | Administration | Manage records | Billing | Help | Contact
Footer: Customer logos | Awards | Terms & Conditions | Privacy
To provide the best support for you to come up with a strong design proposal I will provide DAILY feedback to all participants. We have also created concept mockups (attached) and example pages (below) for each section to give you a clear sense of what we look for.
The core concepts for a successful bid are that the website is EASY to understand, INTUITIVE to navigate, and SIMPLE to use. Most of our users lack technical background and are looking for tool to simplify their work.
The strongest participants (winner and close contenders) will have the opportunity to additional commissioned work on additional sections not included in this brief.
Example Pages (by section)
1. http://www.brovendale.example/site-keepers/
1. http://www.qvt.example/
1. http://www.mondaph.example/
1. http://www.gorvanquest.example/
2. http://www.snapveld.example/profile_edit.gne
3. https://www.tarn.example/how-it-works/
3. http://www.bulkvue.example/learn
4. http://www.pactheron.example/crm/editions-pricing.jsp
4. http://www.brovendale.example/site-keepers/prices
6. https://support.talvora.example/en-gb/
6. http://help.dealmeadow.example/contact_us
8. https://www.careweave.example/uas/login
8. https://www.dealmeadow.example/login
8. http://www.askhollow.example/login/index
For form designs we like Verindo, Bidnook, Snapveld, CareWeave, Chatterly and the concepts presented by Tomas Kerrigan in his classic Layout Craft Shaping the Input Boxes.
For additional guidance see mockups attached!
Target Market(s)
Security, human resources and admin support employees for train operators.
Industry/Entity Type
Learn
Requirements
Should not have
- Home page should not have
Social media icons (chatterly, chirpla, CareWeave, RSS feed)
Contact forms
Read more links
Old trains

```html
<!DOCTYPE html>
<html lang="en">
<head>
<meta charset="utf-8">
<title>tracklo – Point of benefits</title>
<link rel="stylesheet" href="https://fonts.googleapis.com/css2?family=Open+Sans:wght@400;600;700;800&display=swap">
<style>
:root{
  --red:#e0301e;
  --ink:#222;
  --grey:#666;
  --box:#e3e3e3;
  --dark:#1d1d1d;
  --footer:#202020;
  --footer-line:#333;
  --photo:#555;
  --white:#fff;
}
*{box-sizing:border-box;margin:0;padding:0}
html,body{width:673px;height:1200px;overflow:hidden;background:var(--white);font-family:"Open Sans",Arial,sans-serif;color:var(--ink)}
.page{position:relative;width:673px;height:1200px}
.abs{position:absolute}

.topbar{left:0;top:0;width:673px;height:16px;background:var(--dark);color:#aaa;font-size:6px;line-height:16px;padding:0 14px;display:flex;justify-content:space-between}
.topbar .hl{color:var(--white)}

.header{left:0;top:16px;width:673px;height:47px;background:var(--white)}
.brand-name{left:154px;top:12px;font-size:22px;font-weight:800;color:var(--red);letter-spacing:-0.5px;line-height:26px}
.nav{left:282px;top:14px;display:flex;font-size:6.5px;font-weight:700}
.nav a{display:block;padding:6px 7px;color:var(--ink);text-decoration:none}
.nav a.active{background:var(--red);color:var(--white)}
.dropdown{left:449px;top:62px;width:48px;background:var(--white);box-shadow:0 2px 4px rgba(0,0,0,.25);z-index:3;font-size:5px;color:var(--grey)}
.dropdown span{display:block;padding:4px 5px;border-bottom:1px solid #eee}

.hero{left:0;top:63px;width:673px;height:160px;background:linear-gradient(180deg,#8d8d8d 0%,#4c4c4c 55%,#2a2a2a 100%)}
.hero-arrow{top:125px;width:14px;height:14px;border-radius:2px;background:rgba(0,0,0,.6)}
.banner{left:212px;top:205px;width:250px;height:36px;background:var(--red);color:var(--white);font-size:22px;font-weight:800;text-align:center;line-height:36px;box-shadow:0 3px 5px rgba(0,0,0,.3)}

.benefits{left:152px;top:266px;width:375px;display:grid;grid-template-columns:repeat(4,86px);column-gap:10px;row-gap:26px}
.benefit{height:96px;background:var(--box);text-align:center;padding:6px 5px}
.benefit.featured{background:var(--dark);color:var(--white)}
.benefit svg{width:26px;height:26px;display:block;margin:0 auto 4px}
.benefit h3{font-size:5.5px;font-weight:700;margin-bottom:3px}
.benefit p{font-size:4.5px;line-height:6px;color:var(--grey)}
.benefit.featured p{color:#bbb}

.signup{left:0;top:508px;width:673px;text-align:center;font-size:15px;font-weight:800;color:var(--red)}
.welcome{left:0;top:547px;width:673px;text-align:center;font-size:6px;font-style:italic;color:var(--grey)}
.how-title{left:0;top:580px;width:673px;text-align:center;font-size:21px;font-weight:800;color:var(--red)}

.step-shot{width:176px;height:123px;background:var(--photo);border:4px solid var(--white);box-shadow:0 2px 5px rgba(0,0,0,.35);display:flex;align-items:center;justify-content:center}
.step-shot .plus{width:18px;height:18px;border-radius:50%;background:var(--white);color:var(--photo);font-weight:800;font-size:14px;line-height:17px;text-align:center}
.step-text{width:130px}
.step-text h4{font-size:6.5px;font-weight:700;margin-bottom:3px}
.step-text p{font-size:4.5px;line-height:6px;color:var(--grey)}

.more{left:329px;top:1012px;width:15px;height:15px;border-radius:50%;background:var(--dark)}
.more-text{left:0;top:1030px;width:673px;text-align:center;font-size:4.5px;color:var(--grey)}

.footer{left:0;top:1043px;width:673px;height:157px;background:var(--footer);color:#aaa}
.footer h5{font-size:8px;font-weight:700;color:var(--white);margin-bottom:5px}
.footer p{font-size:4.5px;line-height:6.5px}
.field{display:flex;align-items:center;margin-bottom:4px;font-size:5px;color:#ccc}
.field span{width:40px}
.field i{display:block;width:55px;height:9px;background:#3a3a3a}
.send{margin-left:40px;width:34px;height:9px;background:#444;color:var(--white);font-size:4.5px;line-height:9px;text-align:center}
.post{display:flex;gap:5px;margin-bottom:6px}
.post b{display:block;width:26px;height:17px;background:linear-gradient(135deg,#6a8a5a,#3d5a36);flex:none}
.post p{font-size:4.5px}
.post strong{color:var(--red);font-weight:600;display:block;font-size:5px}
.cust-logos{display:flex;gap:6px}
.cust-logos span{display:block;width:24px;height:18px;background:#3a3a3a}
.bottombar{left:0;top:1186px;width:673px;height:14px;background:#161616;border-top:1px solid var(--footer-line);font-size:4.5px;color:#888;line-height:13px;padding:0 20px;display:flex;justify-content:space-between}
.bottombar nav span{margin-left:8px}
</style>
</head>
<body>
<div class="page">

  <div class="abs topbar"><span>Tracklo records made simple for every train operator team</span><span class="hl">Driver help desk</span></div>

  <header class="abs header" aria-label="Site header"></header>
  <div class="abs brand-name">tracklo</div>
  <nav class="abs nav">
    <a>HOME</a><a>OVERVIEW</a><a>PRICES</a><a class="active">HOW IT WORKS?</a><a>ABOUT US</a><a>CONTACT</a>
  </nav>
  <div class="abs dropdown"><span>Step one</span><span>Step two</span><span>Step three</span></div>

  <div class="abs hero" role="img" aria-label="Photo of staff working at a control room desk with monitors"></div>
  <div class="abs hero-arrow" style="left:504px"></div>
  <div class="abs hero-arrow" style="left:520px"></div>
  <div class="abs banner">Point of benefits</div>

  <section class="abs benefits">
    <div class="benefit">
      <svg viewBox="0 0 26 26"><rect x="5" y="6" width="16" height="14" rx="2" fill="#555"/><rect x="8" y="9" width="10" height="2" fill="#ccc"/><rect x="8" y="13" width="7" height="2" fill="#ccc"/></svg>
      <h3>BUILT IN SHORTCODES</h3><p>Keep every driver record tidy and easy to find in one place.</p>
    </div>
    <div class="benefit">
      <svg viewBox="0 0 26 26"><circle cx="13" cy="13" r="8" fill="#555"/><circle cx="13" cy="13" r="3" fill="#ddd"/></svg>
      <h3>ADVANCED OPTIONS</h3><p>Set user rights so each team sees only what it needs.</p>
    </div>
    <div class="benefit featured">
      <svg viewBox="0 0 26 26"><rect x="4" y="7" width="18" height="12" rx="1" fill="#ddd"/><rect x="7" y="10" width="12" height="6" fill="#777"/></svg>
      <h3>TWO SLIDERS</h3><p>Search and filter long lists of drivers in a few clicks.</p>
    </div>
    <div class="benefit">
      <svg viewBox="0 0 26 26"><rect x="6" y="5" width="14" height="16" rx="1" fill="#555"/><rect x="9" y="8" width="8" height="2" fill="#ccc"/><rect x="9" y="12" width="8" height="2" fill="#ccc"/></svg>
      <h3>TWO PORTFOLIO STYLES</h3><p>View records as a list or open a single full profile.</p>
    </div>
    <div class="benefit">
      <svg viewBox="0 0 26 26"><rect x="5" y="6" width="16" height="14" rx="2" fill="#555"/><rect x="8" y="9" width="10" height="2" fill="#ccc"/><rect x="8" y="13" width="7" height="2" fill="#ccc"/></svg>
      <h3>BUILT IN SHORTCODES</h3><p>Create, edit and delete records with clear simple forms.</p>
    </div>
    <div class="benefit">
      <svg viewBox="0 0 26 26"><circle cx="13" cy="13" r="8" fill="#555"/><circle cx="13" cy="13" r="3" fill="#ddd"/></svg>
      <h3>ADVANCED OPTIONS</h3><p>Track licences and training dates without extra paperwork.</p>
    </div>
    <div class="benefit">
      <svg viewBox="0 0 26 26"><rect x="4" y="7" width="18" height="12" rx="1" fill="#555"/><rect x="7" y="10" width="12" height="6" fill="#ccc"/></svg>
      <h3>TWO SLIDERS</h3><p>Friendly screens built for people with no technical skills.</p>
    </div>
    <div class="benefit">
      <svg viewBox="0 0 26 26"><rect x="6" y="5" width="14" height="16" rx="1" fill="#555"/><rect x="9" y="8" width="8" height="2" fill="#ccc"/><rect x="9" y="12" width="8" height="2" fill="#ccc"/></svg>
      <h3>TWO PORTFOLIO STYLES</h3><p>Secure access keeps personal data safe at every step.</p>
    </div>
  </section>

  <div class="abs signup">Sign up or request a call</div>
  <div class="abs welcome">Welcome to Tracklo – a simple place for Tracklo Management. This is a short line that says what you get.</div>
  <div class="abs how-title">how it works? - Have a look</div>

  <div class="abs step-shot" style="left:156px;top:616px" role="img" aria-label="Screenshot of creating a driver record"><span class="plus">+</span></div>
  <div class="abs step-text" style="left:196px;top:746px"><h4>DESCRIPTION TYPE 1</h4><p>Add a new driver and fill in the basic details. Save it in seconds.</p></div>

  <div class="abs step-shot" style="left:350px;top:664px" role="img" aria-label="Screenshot of editing a driver record"><span class="plus">+</span></div>
  <div class="abs step-text" style="left:390px;top:794px"><h4>DESCRIPTION TYPE 2</h4><p>Edit records at any time and keep every licence date up to date.</p></div>

  <div class="abs step-shot" style="left:156px;top:796px" role="img" aria-label="Screenshot of searching the record list"><span class="plus">+</span></div>
  <div class="abs step-text" style="left:196px;top:926px"><h4>DESCRIPTION TYPE 3</h4><p>Search the list by name or depot to find the right driver fast.</p></div>

  <div class="abs step-shot" style="left:350px;top:846px" role="img" aria-label="Screenshot of user rights settings"><span class="plus">+</span></div>
  <div class="abs step-text" style="left:390px;top:976px"><h4>DESCRIPTION TYPE 4</h4><p>Give each user the right access and manage all rights from one page.</p></div>

  <svg class="abs" style="left:0;top:0" width="673" height="1043" viewBox="0 0 673 1043" fill="none" stroke="#e0301e" stroke-width="4" stroke-linecap="round" stroke-linejoin="round">
    <line x1="338" y1="630" x2="362" y2="652"/><polyline points="352,651 362,652 361,642"/>
    <line x1="344" y1="776" x2="300" y2="784"/><polyline points="307,778 300,784 308,790"/>
    <line x1="304" y1="962" x2="342" y2="946"/><polyline points="333,943 342,946 338,955"/>
  </svg>

  <div class="abs more"></div>
  <div class="abs more-text">view more steps</div>

  <footer class="abs footer">
    <div class="abs" style="left:20px;top:12px;width:170px">
      <h5>AWARDS</h5>
      <p>Our tools have been praised by rail teams for clear design and easy daily use across many depots and offices in the region.</p>
      <h5 style="margin-top:14px">CUSTOMER LOGO</h5>
      <div class="cust-logos"><span></span><span></span><span></span><span></span></div>
    </div>
    <div class="abs" style="left:262px;top:12px;width:150px">
      <h5>COMPANY REGISTRATION</h5>
      <div class="field"><span>Name:</span><i></i></div>
      <div class="field"><span>Email:</span><i></i></div>
      <div class="field"><span>Message:</span><i style="height:18px"></i></div>
      <div class="send">Send Message</div>
    </div>
    <div class="abs" style="left:480px;top:12px;width:175px">
      <h5>LATEST POSTS</h5>
      <div class="post"><b role="img" aria-label="Post thumbnail"></b><p><strong>New record tools</strong>Faster forms for busy teams.</p></div>
      <div class="post"><b role="img" aria-label="Post thumbnail"></b><p><strong>User rights update</strong>Simpler roles for every admin.</p></div>
      <div class="post"><b role="img" aria-label="Post thumbnail"></b><p><strong>Pricing made clear</strong>Plans for every operator size.</p></div>
    </div>
  </footer>
  <div class="abs bottombar"><span>© tracklo management</span><nav><span>HOME</span><span>FEATURES</span><span>CONTACT</span><span>TERMS</span></nav></div>

</div>
</body>
</html>
```